Illustration For Couples Game - Fun, Edgy, Smart Design

This is a game for couples that is focused on helping them connect on every level... emotional, mental, spiritual, physical, etc. This image is for the back of the cards. I attached the front and it would be awesome if your design for the back worked with the front. If you don't think your idea will work with the front, I am open to a new idea for a different front.

Target Market(s)

middle class women and men from 25-55

Industry/Entity Type

Online Store

Colors
e34297
b768aa
ec1f27
a54499
e667a6
f04a50

Requirements
Must have
• The background needs to be black. For the coloring, red, white, pink, purple are all great. I don't think colors outside of that will work very well but if you feel inspired with other colors I am somewhat open to other colors. Please have the title "Ember Tales" then "For Couples" as more of a subtitle. Something that is slightly italic and has some shading or outlining might be great, just so that it looks very professional. The dimensions should be 5 inches tall and 3.5 inches wide (sorry not sure about CM). **Also, please have only CMYK designs, thank you!**
Nice to have
• Smart and creative designs that make people think and have depth is great. I actually ran another contest on another site and narrowed down to a few ideas.
• -I like the image of the heart as a lock with a key unlocking it.
• -Also a light bulb shaped as a heart that is turned on
• -Dandelion seeds with hearts attached to them (see example)
• I am open to other images but I know I like these three for sure.
Should not have
• Not overtly sexual since this has more of an emphasis on emotional intimacy than physical. We have found overtly sexual confuses people.

```html
<!DOCTYPE html>
<html lang="en">
<head>
<meta charset="utf-8">
<title>Ember Tales – Couples Card Set</title>
<link href="https://fonts.googleapis.com/css2?family=Arimo:wght@400;700&family=Satisfy&family=Cinzel:wght@400&display=swap" rel="stylesheet">
<style>
  :root {
    --page-bg: #e9e4e2;
    --card-pink: #f2a9d3;
    --card-pink-light: #f8c6e3;
    --card-pink-deep: #e667a6;
    --ink-maroon: #6e0f3d;
    --title-plum: #6a1240;
    --card-black: #1b1b1d;
    --card-black-soft: #2a2a2d;
    --frame-white: #f4f4f4;
    --accent-pink: #e34297;
    --accent-red: #ec1f27;
    --accent-purple: #a54499;
  }
  * { box-sizing: border-box; margin: 0; padding: 0; }
  html, body {
    width: 1200px;
    height: 813px;
    overflow: hidden;
    background: var(--page-bg);
  }
  .card-set {
    width: 1200px;
    height: 813px;
    display: flex;
    justify-content: center;
    align-items: center;
    gap: 60px;
  }
  .card {
    position: relative;
    width: 490px;
    height: 700px;
    border-radius: 26px;
    overflow: hidden;
    box-shadow: 0 10px 28px rgba(0,0,0,0.18);
  }

  /* Front: activity card */
  .card--front {
    background: linear-gradient(160deg, var(--card-pink-light) 0%, var(--card-pink) 55%, #ee9fcb 100%);
  }
  .front__dandelion-top {
    position: absolute;
    top: -20px;
    left: -10px;
    width: 150px;
    height: 220px;
    background: radial-gradient(circle at 50% 30%, rgba(255,255,255,0.75) 0%, rgba(255,255,255,0.2) 45%, rgba(255,255,255,0) 70%);
  }
  .front__dandelion-bottom {
    position: absolute;
    right: 10px;
    bottom: 0;
    width: 170px;
    height: 160px;
    background: radial-gradient(circle at 50% 45%, rgba(255,255,255,0.75) 0%, rgba(255,255,255,0.2) 45%, rgba(255,255,255,0) 70%);
  }
  .front__title {
    position: absolute;
    top: 46px;
    left: 0;
    right: 0;
    text-align: center;
    font-family: "Satisfy", cursive;
    font-size: 74px;
    color: var(--title-plum);
    line-height: 1;
  }
  .front__body {
    position: absolute;
    top: 150px;
    left: 52px;
    right: 52px;
    text-align: center;
    font-family: "Arimo", Arial, sans-serif;
    font-size: 16.5px;
    line-height: 1.42;
    color: var(--ink-maroon);
  }
  .front__brand {
    position: absolute;
    left: 40px;
    bottom: 34px;
    font-family: "Satisfy", cursive;
    font-size: 22px;
    color: var(--ink-maroon);
  }

  /* Back: deck back */
  .card--back {
    background: radial-gradient(ellipse at 50% 40%, var(--card-black-soft) 0%, var(--card-black) 75%);
  }
  .back__frame {
    position: absolute;
    inset: 0;
  }
  .back__emblem {
    position: absolute;
    top: 150px;
    left: 50%;
    transform: translateX(-50%);
    width: 200px;
    height: 120px;
    border-radius: 60px;
    background: radial-gradient(ellipse at center, rgba(227,66,151,0.45) 0%, rgba(165,68,153,0.2) 50%, rgba(27,27,29,0) 75%);
  }
  .back__title {
    position: absolute;
    top: 300px;
    left: 0;
    right: 0;
    text-align: center;
    font-family: "Satisfy", cursive;
    font-size: 78px;
    color: var(--frame-white);
    line-height: 1;
  }
  .back__subtitle {
    position: absolute;
    top: 400px;
    left: 0;
    right: 0;
    text-align: center;
    font-family: "Cinzel", serif;
    font-size: 26px;
    letter-spacing: 6px;
    color: var(--accent-pink);
  }
</style>
</head>
<body>
<main class="card-set">

  <article class="card card--front">
    <div class="front__dandelion-top" role="img" aria-label="Dandelion with heart-shaped seeds drifting"></div>
    <div class="front__dandelion-bottom" role="img" aria-label="Dandelion with heart-shaped seeds drifting"></div>
    <h1 class="front__title">Appreciate</h1>
    <p class="front__body">Everyone likes to be appreciated. This week focus on becoming aware of your partner's many contributions to your life. Notice the little and big things and cultivate an intention to appreciate your partner in ways you seldom acknowledge. Is there an appreciation that you stubbornly hold back on because you feel jealous or have other feelings of insecurity around it? Make an extra effort to acknowledge these contributions from your beloved. Practice expressing your gratitude throughout the day whenever you become aware of feeling thankful. In addition, set aside a few minutes as you go to bed to acknowledge at least five of your lover's gestures, behaviors, words, or acts that made you feel good. If you are having trouble finding things to acknowledge, then focus on why you got together in the first place and then switch your thoughts to a more positive perspective. Once you shift to a more optimistic mindset, there should be plenty of reasons to appreciate your partner.</p>
    <span class="front__brand">Ember Tales</span>
  </article>

  <article class="card card--back">
    <svg class="back__frame" width="490" height="700" viewBox="0 0 490 700" aria-hidden="true">
      <g fill="none" stroke="var(--frame-white)" stroke-width="2" stroke-linecap="round">
        <rect x="34" y="34" width="422" height="632" rx="6"/>
        <path d="M24 70 V24 H70"/>
        <path d="M420 24 H466 V70"/>
        <path d="M24 630 V676 H70"/>
        <path d="M466 630 V676 H420"/>
      </g>
    </svg>
    <div class="back__emblem" role="img" aria-label="Illustration of two hearts joined together"></div>
    <h2 class="back__title">Ember Tales</h2>
    <p class="back__subtitle">FOR COUPLES</p>
  </article>

</main>
</body>
</html>
```